Need a logo/cover design for my book Golden Handshake Hours: How We Turned Coffee Chats Into Fortunes With Friends Worth Keeping

Over the years I've worked in chambers of commerce and at high-profile country clubs and have had access to very successful people and the companies they work for or launch. Through meeting people, learning from them, applying what I've learned, and by connecting with them as resources and lead sources for business, I've been able to generate over $2M in the past few years. I'm sharing the roadmap I followed to create the connections and make the sales.
Updates

Combination of slow feedback on my part by not understanding the process, similar designs, and many who withdrew immediately after my first response.

Target Market(s)

Entrepreneurs and business people, specifically business owners and those in sales and marketing roles.

Industry/Entity Type

Small Business

Font styles to use
Sans Serif

Colors

Designer to choose colors to be used in the design.

Requirements
Must have
• Original graphic design. Something that looks like I paid a professional to have it done.
Nice to have
• Perhaps my picture? Not really sure
Should not have
• I'd like to avoid a look that I could have created myself using clip art and special fonts.

```html
<!DOCTYPE html>
<html lang="en">
<head>
<meta charset="utf-8">
<title>Golden Handshake Hours – Book Cover</title>
<link rel="stylesheet" href="https://fonts.googleapis.com/css2?family=Open+Sans:wght@400;600;700;800&display=swap">
<style>
  :root {
    --backdrop: #dfe5e9;
    --paper: #ffffff;
    --paper-tint: #f0f1f8;
    --title-red: #960a0a;
    --money-green: #1a8a2a;
    --money-green-dark: #0f6b1e;
    --photo-red: rgba(201, 82, 90, 0.85);
    --photo-violet: rgba(183, 166, 214, 0.8);
    --photo-navy: rgba(44, 53, 82, 0.85);
    --photo-skin: rgba(201, 143, 111, 0.95);
    --photo-steel: rgba(120, 145, 190, 0.7);
    --photo-glow: rgba(255, 230, 245, 0.9);
  }
  * { box-sizing: border-box; margin: 0; padding: 0; }
  html, body {
    width: 1200px;
    height: 1200px;
    overflow: hidden;
    background: var(--backdrop);
    font-family: "Open Sans", Arial, sans-serif;
  }
  .book-cover {
    position: absolute;
    left: 255px;
    top: 100px;
    width: 690px;
    height: 1034px;
    background: linear-gradient(180deg, var(--paper) 0%, var(--paper-tint) 50%, var(--paper) 90%);
    box-shadow: 0 6px 24px rgba(40, 50, 70, 0.25);
    text-align: center;
    color: var(--title-red);
    overflow: hidden;
  }
  .book-title span { display: block; }
  .title-top {
    position: absolute;
    top: 108px;
    left: 0;
    width: 100%;
    font-weight: 700;
    font-size: 104px;
    line-height: 1;
    letter-spacing: -1px;
  }
  .title-main {
    position: absolute;
    top: 232px;
    left: 0;
    width: 100%;
    font-weight: 700;
    font-size: 108px;
    line-height: 1;
    letter-spacing: -3px;
    background: linear-gradient(160deg, var(--money-green) 0%, var(--money-green-dark) 50%, var(--money-green) 100%);
    -webkit-background-clip: text;
    background-clip: text;
    -webkit-text-fill-color: transparent;
  }
  .title-bottom {
    position: absolute;
    top: 392px;
    left: 0;
    width: 100%;
    font-weight: 700;
    font-size: 44px;
    line-height: 1;
    letter-spacing: 12px;
    padding-left: 12px;
  }
  .subtitle {
    position: absolute;
    top: 480px;
    left: 40px;
    width: 610px;
    font-size: 19px;
    line-height: 26px;
    font-weight: 400;
    letter-spacing: -0.2px;
  }
  .subtitle strong { font-weight: 700; }
  .cover-photo {
    position: absolute;
    left: 0;
    top: 530px;
    width: 690px;
    height: 400px;
    background:
      radial-gradient(ellipse 90px 70px at 52% 50%, var(--photo-glow), transparent 70%),
      radial-gradient(ellipse 170px 130px at 60% 62%, var(--photo-skin), transparent 75%),
      radial-gradient(ellipse 180px 150px at 44% 75%, var(--photo-navy), transparent 75%),
      radial-gradient(ellipse 200px 160px at 78% 40%, var(--photo-steel), transparent 75%),
      radial-gradient(ellipse 240px 150px at 14% 52%, var(--photo-red), transparent 80%),
      linear-gradient(90deg, var(--photo-red) 0%, var(--photo-violet) 35%, rgba(230, 215, 235, 0.6) 60%, var(--photo-steel) 100%);
    -webkit-mask-image: linear-gradient(180deg, transparent 0%, #000 32%, #000 72%, transparent 100%);
    mask-image: linear-gradient(180deg, transparent 0%, #000 32%, #000 72%, transparent 100%);
  }
  .photo-sweep {
    position: absolute;
    left: 0;
    top: 530px;
    width: 690px;
    height: 400px;
  }
  .author-line {
    position: absolute;
    top: 942px;
    left: 0;
    width: 100%;
    font-size: 48px;
    line-height: 1;
    letter-spacing: 4px;
  }
  .author-first { font-weight: 700; }
  .author-last { font-weight: 400; }
</style>
</head>
<body>
  <main class="book-cover">
    <h1 class="book-title">
      <span class="title-top">GOLDEN</span>
      <span class="title-main">Handshake</span>
      <span class="title-bottom">HOURS</span>
    </h1>
    <p class="subtitle">HOW WE TURNED <strong>COFFEE CHATS INTO FORTUNES</strong><br><strong>WITH FRIENDS WORTH KEEPING</strong></p>

    <div class="cover-photo" role="img" aria-label="Photo of a business handshake blended with a world map and a network of people icons"></div>
    <svg class="photo-sweep" viewBox="0 0 690 400" aria-hidden="true">
      <defs>
        <filter id="sweepSoft" x="-10%" y="-10%" width="120%" height="120%">
          <feGaussianBlur stdDeviation="6"/>
        </filter>
      </defs>
      <path d="M-20 185 C 110 285, 260 370, 470 385 L 700 395 L 700 420 L -20 420 Z" fill="#ffffff" filter="url(#sweepSoft)"/>
    </svg>

    <p class="author-line"><span class="author-first">AUTHOR</span> <span class="author-last">NAME</span></p>
  </main>
</body>
</html>
```